Maple Dental of Temecula needs a flyer

We need a flyer design for Maple Dental. We are located in the city of Temecula in California. Our dental office does general dentistry, cosmetic dentistry, dental implants, orthodontics, dental sleep apnea and TMJ treatment. We would like to design a flyer that could allow the reader know about our services and let them know that we accept new patients. We also have a new patient special that would included necessary dental x rays and dental exam for only $65. We do accept all major credit cards. Also our office accepts most PPO insurances. You can use some of the photos that are included or use stock photos of the dental procedure (they could be before/after photos).

```html
<!DOCTYPE html>
<html lang="en">
<head>
<meta charset="utf-8">
<title>Maple Dental of Temecula – Flyer</title>
<link rel="stylesheet" href="https://fonts.googleapis.com/css2?family=Oswald:wght@500;600&family=Montserrat:wght@700;800&family=Lato:wght@300;400;700&display=swap">
<style>
  :root {
    --brand-blue: #0c5a91;
    --sky-blue: #1ab0ec;
    --charcoal: #333335;
    --panel-gray: #ebebeb;
    --bar-gray: #a6a7a9;
    --footer-gray: #9b9c9e;
    --ink: #222;
    --white: #fff;
  }
  * { margin: 0; padding: 0; box-sizing: border-box; }
  html, body { width: 928px; height: 1200px; overflow: hidden; background: var(--white); }
  .flyer { position: relative; width: 928px; height: 1200px; overflow: hidden; font-family: 'Lato', sans-serif; color: var(--ink); }
  .backdrop { position: absolute; inset: 0; }

  .brand { position: absolute; right: 41px; top: 46px; text-align: right; }
  .brand-name { font-family: 'Oswald', sans-serif; font-weight: 600; font-size: 57px; line-height: 1; color: var(--brand-blue); letter-spacing: 0.5px; }
  .brand-doctor { font-family: 'Oswald', sans-serif; font-weight: 500; font-size: 19px; color: #555; margin-top: 6px; letter-spacing: 0.3px; }

  .doctor-photo { position: absolute; left: 0; top: 630px; width: 260px; height: 338px; background: linear-gradient(180deg, #e2e2e3 0%, #c4c5c7 50%, #8e8f92 100%); }

  .practice { position: absolute; left: 279px; top: 708px; }
  .practice-lead { font-size: 24px; font-weight: 400; color: #222; line-height: 1.1; }
  .practice-name { font-size: 26px; font-weight: 700; color: var(--sky-blue); line-height: 1.15; }
  .practice-creds { font-size: 17px; color: #222; margin-top: 4px; }

  .badge { position: absolute; top: 827px; width: 122px; height: 122px; border-radius: 50%; display: flex; align-items: center; justify-content: center; text-align: center; font-weight: 700; font-size: 15px; line-height: 1.2; color: #1d1d1d; }
  .badge-cards { left: 280px; background: var(--sky-blue); }
  .badge-ppo { left: 410px; background: var(--bar-gray); }

  .services { position: absolute; left: 590px; top: 690px; color: var(--white); }
  .services-title { font-family: 'Montserrat', sans-serif; font-weight: 700; font-size: 32px; letter-spacing: 6px; }
  .services-list { list-style: none; margin-top: 14px; margin-left: 73px; }
  .services-list li { position: relative; font-size: 21px; font-weight: 300; height: 40px; line-height: 40px; }
  .services-list svg { position: absolute; left: -30px; top: 12px; }

  .offer-label { position: absolute; left: 0; top: 970px; width: 556px; height: 40px; background: var(--bar-gray); color: var(--white); font-family: 'Montserrat', sans-serif; font-weight: 700; font-size: 29px; line-height: 40px; padding-left: 47px; }
  .offer-box { position: absolute; left: 0; top: 1020px; width: 556px; height: 117px; background: var(--brand-blue); color: var(--white); }
  .offer-price { position: absolute; left: 56px; top: 4px; font-family: 'Montserrat', sans-serif; font-weight: 800; font-size: 104px; line-height: 108px; letter-spacing: -2px; }
  .offer-detail { position: absolute; left: 288px; top: 16px; font-size: 23px; font-weight: 400; line-height: 29px; }

  .result { position: absolute; top: 1020px; width: 174px; height: 115px; background: linear-gradient(180deg, #d4aa9c 0%, #c3918a 100%); }
  .result-before { left: 566px; }
  .result-after { left: 754px; }
  .result-tag { position: absolute; left: 0; bottom: 8px; width: 64px; height: 12px; background: var(--brand-blue); color: var(--white); font-family: 'Montserrat', sans-serif; font-weight: 700; font-size: 10px; line-height: 12px; padding-left: 12px; }

  .footer { position: absolute; left: 0; top: 1146px; width: 928px; height: 54px; background: var(--footer-gray); color: var(--white); display: flex; align-items: center; font-size: 15.5px; }
  .footer-item { position: absolute; display: flex; align-items: center; gap: 6px; }
  .footer-address { left: 52px; }
  .footer-phone { left: 508px; }
  .footer-web { left: 671px; }
</style>
</head>
<body>
<main class="flyer">
  <svg class="backdrop" width="928" height="1200" viewBox="0 0 928 1200" xmlns="http://www.w3.org/2000/svg">
    <defs>
      <linearGradient id="familyTones" x1="0" y1="0" x2="0" y2="1">
        <stop offset="0" stop-color="#e8ebef"/>
        <stop offset="0.55" stop-color="#e6dcd3"/>
        <stop offset="1" stop-color="#efe7df"/>
      </linearGradient>
      <path id="headlineArc" d="M20,468 Q464,812 908,468"/>
    </defs>
    <rect class="family-photo" x="0" y="0" width="928" height="680" fill="url(#familyTones)" role="img" aria-label="Photo of a smiling family of four outdoors against a pale sky"/>
    <path class="lower-field" d="M0,517 Q464,820 928,525 L928,1200 L0,1200 Z" fill="var(--panel-gray)"/>
    <path class="services-panel" d="M566,640 L928,500 L928,1010 L566,1010 Z" fill="var(--charcoal)"/>
    <path class="headline-band" d="M0,404 Q464,776 928,404 L928,525 Q464,820 0,517 Z" fill="var(--brand-blue)"/>
    <text font-family="Montserrat, sans-serif" font-weight="700" font-size="41" fill="#fff" letter-spacing="0.5">
      <textPath href="#headlineArc" startOffset="50%" text-anchor="middle">ENHANCE THE LOOK OF YOUR SMILE</textPath>
    </text>
  </svg>

  <header class="brand">
    <div class="brand-name">MAPLE DENTAL</div>
    <div class="brand-doctor">DANIEL MERCER, DDS, FIAO, DADIA</div>
  </header>

  <div class="doctor-photo" role="img" aria-label="Portrait photo of the dentist"></div>

  <section class="practice">
    <p class="practice-lead">Dental Practice of</p>
    <p class="practice-name">Dr. Daniel Mercer</p>
    <p class="practice-creds">DDS, FIAO, DADIA, ICOI</p>
  </section>

  <div class="badge badge-cards">We do accept<br>all major<br>credit cards</div>
  <div class="badge badge-ppo">We also<br>accepts most<br>PPO<br>insurances</div>

  <section class="services">
    <h2 class="services-title">SERVICES</h2>
    <ul class="services-list">
      <li><svg width="16" height="16" viewBox="0 0 16 16"><rect x="1" y="3" width="12" height="12" fill="none" stroke="#fff" stroke-width="1.5"/><path d="M4 8 L7 11 L15 2" fill="none" stroke="#fff" stroke-width="1.8"/></svg>General Dentistry</li>
      <li><svg width="16" height="16" viewBox="0 0 16 16"><rect x="1" y="3" width="12" height="12" fill="none" stroke="#fff" stroke-width="1.5"/><path d="M4 8 L7 11 L15 2" fill="none" stroke="#fff" stroke-width="1.8"/></svg>Cosmetic Dentistry</li>
      <li><svg width="16" height="16" viewBox="0 0 16 16"><rect x="1" y="3" width="12" height="12" fill="none" stroke="#fff" stroke-width="1.5"/><path d="M4 8 L7 11 L15 2" fill="none" stroke="#fff" stroke-width="1.8"/></svg>Dental Implants</li>
      <li><svg width="16" height="16" viewBox="0 0 16 16"><rect x="1" y="3" width="12" height="12" fill="none" stroke="#fff" stroke-width="1.5"/><path d="M4 8 L7 11 L15 2" fill="none" stroke="#fff" stroke-width="1.8"/></svg>Orthodontics</li>
      <li><svg width="16" height="16" viewBox="0 0 16 16"><rect x="1" y="3" width="12" height="12" fill="none" stroke="#fff" stroke-width="1.5"/><path d="M4 8 L7 11 L15 2" fill="none" stroke="#fff" stroke-width="1.8"/></svg>Dental Sleep Apnea</li>
      <li><svg width="16" height="16" viewBox="0 0 16 16"><rect x="1" y="3" width="12" height="12" fill="none" stroke="#fff" stroke-width="1.5"/><path d="M4 8 L7 11 L15 2" fill="none" stroke="#fff" stroke-width="1.8"/></svg>TMJ Treatment</li>
    </ul>
  </section>

  <div class="offer-label">NEW PATIENT OFFER</div>
  <section class="offer-box">
    <div class="offer-price">$65</div>
    <p class="offer-detail">Included necessary<br>dental x rays<br>and dental exam</p>
  </section>

  <div class="result result-before" role="img" aria-label="Close-up photo of a smile before treatment"><span class="result-tag">BEFORE</span></div>
  <div class="result result-after" role="img" aria-label="Close-up photo of the same smile after treatment"><span class="result-tag">AFTER</span></div>

  <footer class="footer">
    <span class="footer-item footer-address">
      <svg width="14" height="18" viewBox="0 0 14 18"><path d="M7 0 C3 0 0 3 0 7 C0 12 7 18 7 18 C7 18 14 12 14 7 C14 3 11 0 7 0 Z M7 10 A3 3 0 1 1 7 4 A3 3 0 1 1 7 10 Z" fill="#fff"/></svg>
      1840 Vineyard Park Rd #210 Temecula, CA 92590
    </span>
    <span class="footer-item footer-phone">
      <svg width="12" height="18" viewBox="0 0 12 18"><path d="M3 1 L6 1 L6 5 L4 6 C4 9 5 12 7 13 L9 12 L11 15 L9 17 C4 17 1 11 1 6 C1 3 2 1 3 1 Z" fill="#fff"/></svg>
      (951) 555-0142
    </span>
    <span class="footer-item footer-web">
      <svg width="18" height="18" viewBox="0 0 18 18" fill="none" stroke="#fff" stroke-width="1.2"><circle cx="9" cy="9" r="8"/><ellipse cx="9" cy="9" rx="3.5" ry="8"/><path d="M1 9 H17 M2.5 5 H15.5 M2.5 13 H15.5"/></svg>
      www.maple-dental.example
    </span>
  </footer>
</main>
</body>
</html>
```